Infographic & Data Visualisation Design for – Australia’s Yearly Harmwatch Review 2026

About Callowmere Institute: Callowmere Institute is an independent non-profit public health organization. We produce Australia’s Yearly Harmwatch Review, which translates verified national mortality data into actionable insights for policymakers, journalists, healthcare workers, and the general public.

Project Goal: We need a suite of high-impact, clean, and authoritative infographics and data visualisations created for Australia’s Yearly Harmwatch Review 2026.

What We Are Providing:

Full Dataset (.xlsx): Complete Excel file containing all 2026 report data.

Data & Chart Guidance Doc (.docx): A summary document detailing each dataset, the core takeaway, and our initial recommendations for chart types (e.g., line graphs, horizontal bar charts, donut charts, metric tiles).

Callowmere Institute Brand Book (.pdf): Complete brand guidelines covering fonts, colors, line weights, and imagery. These guidelines and in particular colours should be used across the infographics.

Previous Year Reference: You can view how last year’s report and graphics here: https://www.callowmere-example.org.au/australias-yearly-harmwatch-review-2025/

Designer Input & Creative Freedom: While we have provided a guide suggesting specific chart types for each dataset, we are not data visualisation experts - you are! We are very open to your creative ideas, structural suggestions, and design expertise. If you identify a clearer, more engaging, or visually compelling way to illustrate a specific dataset, we welcome your input.

Required Deliverables:

Master Report Infographics: High-resolution, print/PDF-ready A4 vector graphics for the formal report publication (Delivered as vector AI/EPS and high-res PDF/PNG).

Web Assets: Web-optimized PNG/SVG files with transparent or brand backgrounds.

Social Media Adaptations: 1:1 (Square) and 4:5 / 9:16 (Vertical) graphic cards for Instagram, LinkedIn, Facebook, and X.
Updates

Deadline was too tight - have extended it to ensure the designers have enough time to do the job.

Target Market(s)

Policy makers, journalists, health sector professionals, frontline workers, and the general public.

Industry/Entity Type

Drug/Government/Not for Profit

Font styles to use
Sans Serif
Other font styles liked:
• Brand Fonts: Use any or a combination of: Host Grotesk or Libre Baskerville or Poppins or Calibri Light

Colors

Designer to choose colors to be used in the design.

Requirements
Must have
• The ability to create Infographics, graphs of all kinds from data that we have given.
Nice to have
• Help with choosing what infographics/graphs/donuts graphs etc will be best to visualise the data.
Should not have
• A designer who has not made graphs or infographics from Data.

```html
<!DOCTYPE html>
<html lang="en">
<head>
<meta charset="utf-8">
<title>Australia’s Yearly Harmwatch Review 2026 — Callowmere Institute</title>
<link href="https://fonts.googleapis.com/css2?family=Barlow+Condensed:wght@600;700&family=Host+Grotesk:wght@400;500;600;700&display=swap" rel="stylesheet">
<style>
  :root {
    --navy: #0f1c36;
    --teal: #1a8a7e;
    --teal-light: #7cc7b6;
    --purple: #5b3f91;
    --purple-light: #8f7bbf;
    --card-teal: #eef4f4;
    --card-purple: #f3f0f8;
    --ink: #1b2336;
    --muted: #4a5366;
    --rule: #d5dbe0;
    --paper: #fafbfc;
  }
  * { box-sizing: border-box; margin: 0; padding: 0; }
  html, body { width: 800px; height: 1200px; overflow: hidden; background: var(--paper); }
  body { font-family: "Host Grotesk", "Poppins", sans-serif; color: var(--ink); position: relative; }
  .abs { position: absolute; }

  .brand-panel { left: 0; top: 0; width: 215px; height: 322px; }
  .brand-name { left: 18px; top: 30px; display: flex; align-items: center; gap: 10px;
    color: #fff; font-weight: 500; font-size: 17px; letter-spacing: 1.5px; line-height: 1.25; }
  .brand-name .mark { width: 30px; height: 30px; border-radius: 50%; border: 2px solid var(--teal); flex: none; }
  .pillars { left: 24px; top: 104px; width: 116px; }
  .pillar { display: flex; align-items: center; gap: 14px; height: 58px; border-bottom: 1px solid rgba(255,255,255,.22);
    color: #fff; font-size: 10px; font-weight: 600; letter-spacing: .4px; line-height: 1.4; width: 86px; }
  .pillar:last-child { border-bottom: none; }
  .pillar svg { flex: none; }
  .pillar span { white-space: nowrap; }

  .tagline { left: 468px; top: 20px; font-size: 10px; font-weight: 600; letter-spacing: .9px; color: var(--teal);
    padding-bottom: 6px; border-bottom: 1px solid var(--rule); width: 302px; white-space: nowrap; }

  .title { left: 226px; top: 50px; font-family: "Barlow Condensed", sans-serif; font-weight: 700;
    font-size: 58px; line-height: 52px; color: var(--navy); letter-spacing: .5px; }
  .title .year { color: var(--teal); }
  .title-rule { left: 228px; top: 212px; width: 38px; height: 2px; background: var(--teal); }
  .lede { left: 228px; top: 228px; width: 325px; font-size: 12.5px; line-height: 20px; color: var(--ink); }

  .halo { left: 28px; top: 268px; width: 560px; height: 424px; border-radius: 50%;
    background: radial-gradient(circle at 50% 50%, rgba(250,251,252,1) 0 30%, rgba(26,138,126,.22) 42%, rgba(91,63,145,.16) 58%, rgba(91,63,145,.05) 72%, rgba(250,251,252,0) 80%); }
  .hero { left: 170px; top: 390px; width: 286px; text-align: center; }
  .hero .when { font-size: 12.5px; font-weight: 500; color: var(--teal); letter-spacing: 1px; }
  .hero .when::after { content: ""; display: block; width: 26px; height: 1.5px; background: var(--teal); margin: 5px auto 0; }
  .hero .count { font-family: "Barlow Condensed", sans-serif; font-weight: 700; font-size: 112px; line-height: 100px;
    color: var(--teal); letter-spacing: -1px; margin-top: 2px; }
  .hero .lost { font-family: "Barlow Condensed", sans-serif; font-weight: 600; font-size: 23px; line-height: 25px; color: var(--navy); margin-top: 6px; }
  .hero .cause { font-size: 11px; color: var(--teal); margin-top: 5px; }

  .pill { left: 209px; top: 645px; width: 203px; height: 46px; border-radius: 23px; background: var(--navy);
    display: flex; align-items: center; gap: 10px; padding-left: 14px; color: #fff; font-size: 11px; line-height: 16px; }
  .pill em { font-style: normal; color: var(--teal-light); }

  .impact-head { left: 622px; top: 225px; font-size: 13px; font-weight: 600; color: var(--teal); letter-spacing: .3px; }
  .impact-head::after { content: ""; display: block; width: 32px; height: 2px; background: var(--teal); margin-top: 8px; }
  .impact-card { left: 614px; width: 163px; border-radius: 10px; }
  .impact-card .icon { position: absolute; left: 15px; width: 46px; height: 46px; border-radius: 50%;
    display: flex; align-items: center; justify-content: center; }
  .impact-card .txt { position: absolute; left: 80px; }
  .impact-card .lbl { font-size: 10px; font-weight: 600; color: var(--navy); letter-spacing: .2px; white-space: nowrap; }
  .impact-card .num { font-family: "Barlow Condensed", sans-serif; font-weight: 700; font-size: 54px; line-height: 50px; margin-top: 2px; }
  .impact-card .unit { font-size: 11px; font-weight: 600; color: var(--navy); letter-spacing: .4px; margin-top: 2px; }
  .impact-card .sub { font-size: 9px; color: var(--muted); margin-top: 7px; }
  .card-week { top: 266px; height: 137px; background: var(--card-teal); }
  .card-day { top: 417px; height: 136px; background: var(--card-purple); }
  .card-hour { top: 569px; height: 133px; background: var(--card-teal); }
  .teal-num { color: var(--teal); }
  .purple-num { color: var(--purple); }

  .divider { left: 25px; top: 721px; width: 752px; height: 1px; background: var(--rule); }
  .vdivider { left: 465px; top: 738px; width: 1px; height: 270px; background: var(--rule); }

  .section-head { font-size: 12px; font-weight: 600; color: var(--teal); letter-spacing: .3px; line-height: 18px; }

  .state-map { left: 112px; top: 768px; width: 238px; height: 188px; border-radius: 42% 38% 36% 44%;
    background: linear-gradient(135deg, #8ecfbd 0%, #5aa9a0 40%, #2f5c6e 70%, #6a55a6 100%); opacity: .9; z-index: 0; }
  .state-island { left: 292px; top: 986px; width: 18px; height: 16px; border-radius: 50%; background: #6fbfae; z-index: 0; }
  .state-tag { z-index: 2; }
  .state-label { font-size: 8px; font-weight: 600; color: var(--navy); line-height: 11.5px; letter-spacing: .2px; }
  .state-value { font-family: "Barlow Condensed", sans-serif; font-weight: 600; font-size: 20px; color: var(--teal); line-height: 22px; }
  .leaders { left: 0; top: 0; width: 800px; height: 1200px; pointer-events: none; z-index: 1; }

  .substances { left: 485px; top: 740px; width: 260px; }
  .sub-row { position: absolute; left: 0; width: 260px; height: 44px; display: flex; align-items: center; }
  .sub-row .rank { width: 24px; height: 24px; border-radius: 50%; color: #fff; font-size: 12px; font-weight: 600;
    display: flex; align-items: center; justify-content: center; flex: none; }
  .sub-row .ico { width: 39px; height: 39px; border-radius: 50%; margin-left: 14px; flex: none;
    display: flex; align-items: center; justify-content: center; }
  .sub-row .name { margin-left: 18px; font-size: 11px; line-height: 14px; color: var(--navy); width: 110px; }
  .sub-row .val { margin-left: auto; font-family: "Barlow Condensed", sans-serif; font-weight: 600; font-size: 21px; padding-right: 6px; }
  .sub-row.ruled::after { content: ""; position: absolute; left: 38px; right: 0; bottom: -1px; height: 1px; background: var(--rule); }
  .bg-teal { background: var(--teal); }
  .bg-purple { background: var(--purple); }
  .soft-teal { background: #e2eeee; }
  .soft-purple { background: #ece7f4; }

  .insight { left: 37px; top: 1027px; width: 733px; height: 117px; border-radius: 14px; background: var(--navy); }
  .insight .emblem { position: absolute; left: 22px; top: 10px; width: 97px; height: 97px; border-radius: 50%;
    border: 1.5px solid rgba(255,255,255,.85); background: radial-gradient(circle, rgba(255,255,255,.12), rgba(255,255,255,0)); }
  .insight .vline { position: absolute; left: 143px; top: 18px; width: 1.5px; height: 82px; background: var(--teal); }
  .insight .kicker { position: absolute; left: 159px; top: 18px; font-family: "Barlow Condensed", sans-serif; font-weight: 600;
    font-size: 18px; line-height: 20px; color: var(--teal-light); letter-spacing: .5px; }
  .insight .head { position: absolute; left: 233px; top: 16px; width: 330px; font-size: 14px; line-height: 20px; color: #fff; font-weight: 500; }
  .insight .body { position: absolute; left: 233px; top: 63px; width: 330px; font-size: 9.5px; line-height: 14px; color: #d9dee8; }
  .insight .dotmap { position: absolute; left: 588px; top: 12px; width: 110px; height: 96px; border-radius: 40% 45% 35% 40%;
    background: radial-gradient(circle at 55% 45%, rgba(124,199,182,.75), rgba(26,138,126,.35) 60%, rgba(15,28,54,0) 75%); }

  .footer-rule { left: 25px; top: 1155px; width: 752px; height: 1px; background: var(--rule); }
  .footer-brand { left: 36px; top: 1166px; display: flex; align-items: center; gap: 9px; font-size: 12.5px; font-weight: 600;
    letter-spacing: 1px; color: var(--navy); white-space: nowrap; }
  .footer-brand .mark { width: 22px; height: 22px; border-radius: 50%; border: 1.5px solid var(--teal); }
  .footer-sep { left: 246px; top: 1164px; width: 1px; height: 26px; background: var(--teal); }
  .footer-url { left: 264px; top: 1171px; font-size: 9.5px; color: var(--teal); }
  .footer-source { right: 37px; top: 1171px; font-size: 9.5px; color: var(--navy); }
  .footer-source b { font-weight: 600; }
</style>
</head>
<body>

  <svg class="abs brand-panel" viewBox="0 0 215 322" aria-hidden="true">
    <path d="M0 0 H212 L146 250 Q124 302 64 312 L0 322 Z" fill="#0f1c36"/>
  </svg>
  <div class="abs brand-name"><span class="mark"></span><span>CALLOWMERE<br>INSTITUTE</span></div>
  <div class="abs pillars">
    <div class="pillar">
      <svg width="28" height="32" viewBox="0 0 28 32"><path d="M14 2 L26 6 V15 C26 23 20 28 14 30 C8 28 2 23 2 15 V6 Z" fill="none" stroke="#1a8a7e" stroke-width="2"/><path d="M8 16 L12.5 20 L20 11" fill="none" stroke="#1a8a7e" stroke-width="2"/></svg>
      <span>EVIDENCE<br>BASED</span>
    </div>
    <div class="pillar">
      <svg width="28" height="28" viewBox="0 0 28 28"><rect x="1" y="16" width="6" height="11" fill="#1a8a7e"/><rect x="11" y="10" width="6" height="17" fill="#1a8a7e"/><rect x="21" y="3" width="6" height="24" fill="#1a8a7e"/></svg>
      <span>DATA<br>DRIVEN</span>
    </div>
    <div class="pillar">
      <svg width="28" height="26" viewBox="0 0 30 26"><circle cx="9" cy="7" r="5" fill="none" stroke="#1a8a7e" stroke-width="1.8"/><circle cx="21" cy="7" r="5" fill="none" stroke="#1a8a7e" stroke-width="1.8"/><path d="M1 25 C1 17 17 17 17 25 M13 25 C13 17 29 17 29 25" fill="none" stroke="#1a8a7e" stroke-width="1.8"/></svg>
      <span>ACTION<br>FOCUSED</span>
    </div>
  </div>

  <div class="abs tagline">INDEPENDENT. EVIDENCE-BASED. ACTION-FOCUSED.</div>

  <h1 class="abs title">AUSTRALIA’S<br>YEARLY HARMWATCH<br>REVIEW <span class="year">2026</span></h1>
  <div class="abs title-rule"></div>
  <p class="abs lede">Drug-induced deaths remain one of Australia’s most significant preventable public health challenges.</p>

  <div class="abs halo" role="img" aria-label="Radiating field of dots, each representing a life lost"></div>
  <div class="abs hero">
    <div class="when">IN 2024</div>
    <div class="count">2,596</div>
    <div class="lost">Australians lost<br>their lives</div>
    <div class="cause">to drug-induced causes</div>
  </div>

  <div class="abs pill">
    <svg width="28" height="24" viewBox="0 0 28 24"><circle cx="14" cy="6" r="4" fill="none" stroke="#fff" stroke-width="1.5"/><circle cx="5" cy="9" r="3" fill="none" stroke="#fff" stroke-width="1.5"/><circle cx="23" cy="9" r="3" fill="none" stroke="#fff" stroke-width="1.5"/><path d="M7 22 C7 13 21 13 21 22 Z M1 21 C1 15 6 14 8 16 M27 21 C27 15 22 14 20 16" fill="none" stroke="#fff" stroke-width="1.5"/></svg>
    <span>Behind every dot is a life.<br><em>Gone too soon.</em></span>
  </div>

  <div class="abs impact-head">THE IMPACT IN TIME</div>

  <div class="abs impact-card card-week">
    <div class="icon bg-teal" style="top:30px">
      <svg width="24" height="24" viewBox="0 0 24 24"><rect x="2" y="4" width="20" height="18" rx="2" fill="none" stroke="#fff" stroke-width="1.8"/><path d="M2 9 H22 M7 1 V6 M17 1 V6" stroke="#fff" stroke-width="1.8"/><g fill="#fff"><rect x="6" y="12" width="3" height="3"/><rect x="11" y="12" width="3" height="3"/><rect x="16" y="12" width="3" height="3"/><rect x="6" y="17" width="3" height="3"/><rect x="11" y="17" width="3" height="3"/></g></svg>
    </div>
    <div class="txt" style="top:22px">
      <div class="lbl">EVERY WEEK</div>
      <div class="num teal-num">50</div>
      <div class="unit">DEATHS</div>
      <div class="sub">Australians lost</div>
    </div>
  </div>

  <div class="abs impact-card card-day">
    <div class="icon bg-purple" style="top:15px">
      <svg width="26" height="26" viewBox="0 0 26 26"><circle cx="13" cy="13" r="11" fill="none" stroke="#fff" stroke-width="1.8"/><path d="M13 6 V13 L18 16" fill="none" stroke="#fff" stroke-width="1.8"/></svg>
    </div>
    <div class="txt" style="top:20px">
      <div class="lbl">EVERY DAY</div>
      <div class="num purple-num">7</div>
      <div class="unit">DEATHS</div>
      <div class="sub">Australians lost</div>
    </div>
  </div>

  <div class="abs impact-card card-hour">
    <div class="icon bg-teal" style="top:15px">
      <svg width="26" height="26" viewBox="0 0 26 26"><circle cx="13" cy="15" r="9.5" fill="none" stroke="#fff" stroke-width="1.8"/><path d="M10 2 H16 M13 2 V5 M13 10 V15 L16 17" fill="none" stroke="#fff" stroke-width="1.8"/></svg>
    </div>
    <div class="txt" style="top:18px;left:72px">
      <div class="lbl">EVERY 3.5 HOURS</div>
      <div class="num teal-num">1</div>
      <div class="unit">DEATH</div>
      <div class="sub">Australians lost</div>
    </div>
  </div>

  <div class="abs divider"></div>

  <div class="abs section-head" style="left:42px;top:737px">DEATHS BY STATE &amp; TERRITORY (2024)</div>
  <div class="abs state-map" role="img" aria-label="Map of Australia shaded by state and territory drug-induced deaths"></div>
  <div class="abs state-island" role="img" aria-label="Tasmania on the state map"></div>

  <svg class="abs leaders" viewBox="0 0 800 1200" aria-hidden="true" fill="none" stroke="#0f1c36" stroke-width="0.8">
    <path d="M104 782 H190 L202 802"/><circle cx="202" cy="802" r="2" fill="#0f1c36"/>
    <path d="M365 796 H332 L308 830"/><circle cx="365" cy="796" r="2" fill="#0f1c36"/>
    <path d="M84 872 H125"/><circle cx="125" cy="872" r="2" fill="#0f1c36"/>
    <path d="M172 974 H208 L234 938"/><circle cx="172" cy="974" r="2" fill="#0f1c36"/>
    <path d="M264 1000 H298 V996"/>
    <path d="M385 929 H338"/>
    <path d="M385 981 H360 L336 948"/>
  </svg>

  <div class="abs state-tag" style="left:45px;top:771px"><div class="state-label">NORTHERN<br>TERRITORY</div><div class="state-value">15</div></div>
  <div class="abs state-tag" style="left:375px;top:778px"><div class="state-label">QUEENSLAND</div><div class="state-value">417</div></div>
  <div class="abs state-tag" style="left:41px;top:849px"><div class="state-label">WESTERN<br>AUSTRALIA</div><div class="state-value">278</div></div>
  <div class="abs state-tag" style="left:385px;top:842px"><div class="state-label">NEW SOUTH<br>WALES</div><div class="state-value">587</div></div>
  <div class="abs state-tag" style="left:388px;top:909px"><div class="state-label">AUSTRALIAN<br>CAPITAL<br>TERRITORY</div><div class="state-value">29</div></div>
  <div class="abs state-tag" style="left:120px;top:957px"><div class="state-label">SOUTH<br>AUSTRALIA</div><div class="state-value">157</div></div>
  <div class="abs state-tag" style="left:226px;top:984px"><div class="state-label">TASMANIA</div><div class="state-value">35</div></div>
  <div class="abs state-tag" style="left:388px;top:975px"><div class="state-label">VICTORIA</div><div class="state-value">572</div></div>

  <div class="abs vdivider"></div>

  <div class="abs section-head" style="left:485px;top:740px">LEADING SUBSTANCES INVOLVED IN<br>UNINTENTIONAL OVERDOSE DEATHS (2024)</div>
  <div class="abs substances" style="top:788px">
    <div class="sub-row ruled" style="top:0">
      <span class="rank bg-teal">1</span>
      <span class="ico soft-teal"><svg width="22" height="22" viewBox="0 0 22 22"><rect x="1" y="7" width="20" height="8" rx="4" transform="rotate(-40 11 11)" fill="none" stroke="#1a8a7e" stroke-width="1.6"/><path d="M8 6 L14 15" stroke="#1a8a7e" stroke-width="1.6"/></svg></span>
      <span class="name">Opioids</span><span class="val teal-num">877</span>
    </div>
    <div class="sub-row ruled" style="top:47px">
      <span class="rank bg-purple">2</span>
      <span class="ico soft-purple"><svg width="20" height="22" viewBox="0 0 20 22"><path d="M10 1 L19 7 L16 20 H4 L1 7 Z M10 1 L7 12 L10 20 L13 12 Z" fill="none" stroke="#5b3f91" stroke-width="1.4"/></svg></span>
      <span class="name">Amphetamine-type stimulants</span><span class="val purple-num">772</span>
    </div>
    <div class="sub-row ruled" style="top:94px">
      <span class="rank bg-teal">3</span>
      <span class="ico soft-teal"><svg width="22" height="22" viewBox="0 0 22 22"><circle cx="11" cy="11" r="9" fill="none" stroke="#1a8a7e" stroke-width="1.6"/><path d="M5 17 L17 5" stroke="#1a8a7e" stroke-width="1.6"/></svg></span>
      <span class="name">Benzodiazepines</span><span class="val teal-num">514</span>
    </div>
    <div class="sub-row ruled" style="top:139px">
      <span class="rank bg-purple">4</span>
      <span class="ico soft-purple"><svg width="14" height="24" viewBox="0 0 14 24"><path d="M5 1 H9 V6 L12 10 V23 H2 V10 L5 6 Z" fill="none" stroke="#5b3f91" stroke-width="1.5"/><rect x="4" y="13" width="6" height="5" fill="#5b3f91"/></svg></span>
      <span class="name">Alcohol</span><span class="val purple-num">311</span>
    </div>
    <div class="sub-row" style="top:182px">
      <span class="rank bg-teal">5</span>
      <span class="ico soft-teal"><svg width="22" height="22" viewBox="0 0 22 22"><path d="M6 21 V16 C2 14 2 8 5 5 C8 1 16 1 18 6 L19 10 L21 12 L19 13 V17 H15 V21" fill="none" stroke="#1a8a7e" stroke-width="1.5"/><circle cx="11" cy="9" r="3" fill="none" stroke="#1a8a7e" stroke-width="1.3"/></svg></span>
      <span class="name">Antidepressants</span><span class="val teal-num">293</span>
    </div>
  </div>

  <div class="abs insight">
    <div class="emblem" role="img" aria-label="Emblem of caring hands supporting a community"></div>
    <div class="vline"></div>
    <div class="kicker">KEY<br>INSIGHT</div>
    <div class="head">More Australians die from drug-induced causes than many people realise.</div>
    <div class="body">The burden is experienced across every state and territory, highlighting the need for evidence-based prevention, treatment and harm reduction responses.</div>
    <div class="dotmap" role="img" aria-label="Dotted map of Australia"></div>
  </div>

  <div class="abs footer-rule"></div>
  <div class="abs footer-brand"><span class="mark"></span>CALLOWMERE INSTITUTE</div>
  <div class="abs footer-sep"></div>
  <div class="abs footer-url">callowmere-example.org.au</div>
  <div class="abs footer-source"><b>Source:</b> Federal Mortality Records Registry (2024).</div>

</body>
</html>
```